Birchwell Entreprise Campus Media Package

We are looking for a designer to unify our company's image throughout its stationery and marketing deliverables. We will be focusing on:
*Business Cards (3.5 x 2)
*Letter Head (Letter Size)
*PowerPoint Presentation Template,
*One Pager Flyer (Letter Size)
*Front of Elevator's bay: 4 photos of the elevator bays (two groups of 3 elevators) to which we are looking for designs for its doors and surrounding wall (vinyl prints)
*Font's suggestions
*Official color palette.
*Outdoor Street Signage: please use the following dimensions:
Sign #1 (Richmond Side): 48(W)x72"(H) (3 sided)
Sign #2: 24"(W)x48"(H) (3 sided)
Sign #3 (Top of Hill): 30(W)x54(H) (2 sides)
*Carport Sign:
See photos attached. The white letters will be removed, and a new sign will take place. Preferably, Cut-Out fonts, but we can consider an alternative approach for cost effective solution.
Find attached the approved logos.
______________________________________
We are a real estate holding company focused on the commercial office space in the Ohio, US, market.
You can check our site at www.birchwellcampus-example.com
As inspiration guidelines, we would like to see designs that are modern, minimalistic, dynamic and energetic.
Updates
Target Market(s)
General Population, Business Owners, Non-Profit Organizations, Government
Industry/Entity Type
Real Estate - Commercial Office Space - Flex Space
Look and feel
Each slider illustrates characteristics of the customer's brand and the style your logo design should communicate.

```html
<!DOCTYPE html>
<html lang="la">
<head>
<meta charset="utf-8">
<title>Typography Sample – Headings and Body</title>
<link rel="stylesheet" href="https://fonts.googleapis.com/css2?family=Aleo:wght@700&family=Carlito:wght@400&display=swap">
<style>
  :root {
    --page-bg: #ffffff;
    --ink: #111111;
    --heading-ink: #151515;
  }
  * { margin: 0; padding: 0; box-sizing: border-box; }
  html, body {
    width: 720px;
    height: 1200px;
    overflow: hidden;
    background: var(--page-bg);
  }
  .type-sheet {
    position: relative;
    width: 720px;
    height: 1200px;
    padding: 84px 86px 0 87px;
    color: var(--ink);
    font-family: "Carlito", "Calibri", sans-serif;
    font-size: 13.2px;
    line-height: 17.6px;
  }
  .heading {
    font-family: "Aleo", "Rockwell", serif;
    font-weight: 700;
    color: var(--heading-ink);
    letter-spacing: -0.01em;
  }
  .heading--one {
    font-size: 29px;
    line-height: 35px;
    margin-bottom: 15px;
    letter-spacing: -0.02em;
  }
  .heading--two {
    font-size: 21px;
    line-height: 26px;
    margin: 12px 0 16px;
  }
  .heading--three {
    font-size: 16px;
    line-height: 20px;
    margin: 15px 0 17px;
  }
  .heading--four {
    font-size: 14px;
    line-height: 18px;
    margin: 16px 0 16px;
  }
  .body-copy {
    margin-bottom: 16px;
  }
  .body-copy:last-child { margin-bottom: 0; }
  .bullet-list {
    list-style: none;
    padding-left: 44px;
    margin: 0 0 0;
  }
  .bullet-list__item {
    position: relative;
  }
  .bullet-list__item::before {
    content: "";
    position: absolute;
    left: -20px;
    top: 7px;
    width: 4.5px;
    height: 4.5px;
    border-radius: 50%;
    background: var(--ink);
  }
</style>
</head>
<body>
<main class="type-sheet">
  <h1 class="heading heading--one">Lorem ipsum for heading</h1>
  <p class="body-copy">Lorem ipsum dolar sit amet voluptatem fugit aut illo omnis explicabo ipsa ipsa, nemo rem ipsam quasi illo dolores ut voluptatem doloremque perspiciatis beatae magni architecto odit odit, aspernatur magni quae aperiam aut veritatis beatae eos aut voluptas doloremque perspiciatis error natus natus, qui aut eaque inventore aut quasi consequuntur consequuntur ipsa aspernatur iste sit sit, quae explicabo dicta quasi</p>
  <p class="body-copy">Lorem ipsum dolor sit amet rem eos illo omnis aut aperiam ab ipsam ipsa odit aut aperiam aut aspernatur veritatis unde unde, sed enim accusantium laudantium laudantium sunt perspiciatis ipsam sed doloremque ipsam dolores totam unde unde, et aut illo aut veritatis explicabo dicta quia dicta veritatis dicta sunt quasi eaque rem eos enim aperiam aperiam, omnis ipsa sed nemo perspiciatis quasi ipsam eos ratione quia quae et aut quia architecto</p>

  <h2 class="heading heading--two">Lorem ipsum for heading two</h2>
  <p class="body-copy">Lorem ipsum dolor sit amet eaque eaque totam ratione voluptas error eaque iste perspiciatis voluptas aut sit odit quasi quasi, unde quasi quae ratione inventore ipsa explicabo iste sunt sed sit ipsam voluptatem consequuntur iste ipsam ipsam consequuntur consequuntur, quia ratione ratione dolores consequuntur ut consequuntur architecto sunt beatae architecto aperiam natus odit ipsa sed quasi quasi, et et beatae eos laudantium quae et explicabo et eos voluptatem quae aspernatur</p>

  <h3 class="heading heading--three">Lorem ipsum for heading three</h3>
  <p class="body-copy">Lorem ipsum dolor sit amet voluptatem natus eos eaque sed dicta dicta, enim quasi ratione aperiam vitae ipsa eos iste unde veritatis magni beatae dicta qui illo totam. Totamaspernatur accusantium sunt laudantium beatae ut laudantium. Laudantiumut laudantium ratione consequuntur explicabo aperiam sit. Siteos aperiam ut eaque qui inventore veritatis aperiam quia quae ut architecto voluptas consequuntur iste sit aut accusantium dolores unde</p>
  <ul class="bullet-list">
    <li class="bullet-list__item">quasi error magni doloremque veritatis illo sed eaque</li>
    <li class="bullet-list__item">inventore quasi explicabo aspernatur accusantium inventore inventore, eaque inventore totam sit</li>
    <li class="bullet-list__item">sed sed qui sed odit quia sed architecto aut eos</li>
    <li class="bullet-list__item">rem odit totam quasi beatae nemo et ratione ratione</li>
    <li class="bullet-list__item">quia veritatis totam ipsa vitae architecto eos sit aut accusantium accusantium,</li>
  </ul>

  <h4 class="heading heading--four">Lorem ipsum for heading four</h4>
  <p class="body-copy">Lorem ipsum dolor sit amet vitae sed et totam aperiam sed consequuntur odit aperiam aperiam, laudantium aut ab voluptatem vitae inventore consequuntur dolores explicabo vitae aut nemo natus voluptatem totam accusantium perspiciatis perspiciatis, veritatis voluptatem sed sunt unde ut. Utvitae consequuntur error. Errorrem eos voluptas ut quasi doloremque beatae unde omnis omnis, sit ipsam enim veritatis dicta ut sed laudantium accusantium sit sit voluptatem rem error voluptatem quasi error error, odit odit quia ipsa laudantium veritatis perspiciatis ipsam rem</p>
</main>
</body>
</html>
```